Offshore Energy Projects Management Consultancy needs a business card design

Logo available. We provide teams to deliver engineering consultancy, project management and delivery teams mainly in the offshore renewables sector. The company is all about bringing the right people to a project to deliver the scope.

The business card will be used for all staff.

The business card should be quite simple, vibrant and uncluttered but convey experience, enthusiasm and integration.

Target Market(s)

Energy Project Developers and Tier 1 construction companies

Contact Information for Business Card

Logo should be on the back of the card. I'm happy for the designer to play with the colour of the logo and background colour.

Front of the card should convey all the must have information in a clear and professional manner but without being overly traditional.

Colors

Designer to choose colors to be used in the design.

Requirements
Must have
• Land Line Tel Number, Mobile Tel Number, Email, business address, web address.

```html
<!DOCTYPE html>
<html lang="en">
<head>
<meta charset="utf-8">
<title>Tidewell Project Partners – Business Card</title>
<link href="https://fonts.googleapis.com/css2?family=Lato:wght@400;700&display=swap" rel="stylesheet">
<style>
  :root {
    --backdrop: #2b2d31;
    --card-white: #ffffff;
    --band-grey: #66686c;
    --accent-blue: #2a9be0;
    --brand-blue: #1f78cc;
    --deep-blue: #1460b4;
    --text-light: #ffffff;
    --text-soft: #e4e6ea;
  }
  html, body {
    margin: 0;
    padding: 0;
    width: 1200px;
    height: 900px;
    overflow: hidden;
    background: var(--backdrop);
    font-family: "Lato", sans-serif;
  }
  .canvas {
    position: relative;
    width: 1200px;
    height: 900px;
  }
  .card {
    position: absolute;
    top: 295px;
    width: 540px;
    height: 310px;
    border-radius: 4px;
    overflow: hidden;
    box-shadow: 0 14px 30px rgba(0,0,0,0.45);
  }
  .card-front { left: 40px; background: var(--card-white); }
  .card-back {
    left: 620px;
    background: radial-gradient(ellipse at 55% 45%, var(--accent-blue) 0%, var(--brand-blue) 55%, var(--deep-blue) 100%);
  }
  .front-shapes {
    position: absolute;
    inset: 0;
  }
  .brand {
    position: absolute;
    display: flex;
    align-items: center;
    gap: 10px;
    white-space: nowrap;
  }
  .brand-dot {
    border-radius: 50%;
    flex: none;
  }
  .brand-name {
    font-weight: 700;
    letter-spacing: 0.5px;
  }
  .card-front .brand { left: 140px; top: 72px; }
  .card-front .brand-dot { width: 22px; height: 22px; background: var(--brand-blue); }
  .card-front .brand-name { font-size: 22px; color: var(--brand-blue); }
  .card-back .brand { left: 0; right: 0; top: 136px; justify-content: center; }
  .card-back .brand-dot { width: 28px; height: 28px; background: var(--text-light); }
  .card-back .brand-name { font-size: 28px; color: var(--text-light); }

  .person {
    position: absolute;
    left: 24px;
    top: 196px;
    color: var(--text-light);
  }
  .person-name { font-size: 17px; font-weight: 700; margin: 0 0 2px; }
  .person-role { font-size: 12px; color: var(--text-soft); margin: 0 0 10px; }
  .person-address { font-size: 12px; color: var(--text-soft); line-height: 1.45; margin: 0; font-style: normal; }

  .divider {
    position: absolute;
    left: 206px;
    top: 196px;
    width: 1px;
    height: 92px;
    background: var(--accent-blue);
  }
  .contacts {
    position: absolute;
    left: 226px;
    top: 194px;
    margin: 0;
    padding: 0;
    list-style: none;
    color: var(--text-light);
    font-size: 14px;
  }
  .contacts li {
    display: flex;
    align-items: center;
    gap: 10px;
    height: 24px;
  }
  .contacts svg { width: 14px; height: 14px; flex: none; }
</style>
</head>
<body>
<main class="canvas">
  <section class="card card-front" aria-label="Business card front">
    <svg class="front-shapes" viewBox="0 0 540 310" width="540" height="310" aria-hidden="true">
      <path d="M0 158 L452 196 Q480 198 492 216 L498 226 Q506 238 522 238 L540 238 L540 310 L0 310 Z" fill="var(--band-grey)"/>
      <path d="M0 150 L452 188 Q480 190 492 208 L498 218 Q506 230 522 230 L540 230" fill="none" stroke="var(--accent-blue)" stroke-width="5"/>
    </svg>

    <div class="brand">
      <span class="brand-dot"></span>
      <span class="brand-name">Tidewell Project Partners</span>
    </div>

    <div class="person">
      <p class="person-name">Marek Jovanic</p>
      <p class="person-role">Managing Director</p>
      <address class="person-address">118 Harbourline Road<br>London EC2 4RT</address>
    </div>

    <span class="divider"></span>

    <ul class="contacts">
      <li>
        <svg viewBox="0 0 16 16" aria-hidden="true"><path d="M3 1.5h3l1.2 3.2-1.8 1.2a8 8 0 0 0 4.7 4.7l1.2-1.8 3.2 1.2v3a1.5 1.5 0 0 1-1.6 1.5A12.5 12.5 0 0 1 1.5 3.1 1.5 1.5 0 0 1 3 1.5z" fill="none" stroke="var(--accent-blue)" stroke-width="1.3"/></svg>
        +44 000 481 7720
      </li>
      <li>
        <svg viewBox="0 0 16 16" aria-hidden="true"><rect x="4.5" y="1" width="7" height="14" rx="1.5" fill="none" stroke="var(--accent-blue)" stroke-width="1.3"/><circle cx="8" cy="12.5" r="0.8" fill="var(--accent-blue)"/></svg>
        +44 000 481 7735
      </li>
      <li>
        <svg viewBox="0 0 16 16" aria-hidden="true"><rect x="1" y="3" width="14" height="10" rx="1" fill="none" stroke="var(--accent-blue)" stroke-width="1.3"/><path d="M1.5 3.5 8 9l6.5-5.5" fill="none" stroke="var(--accent-blue)" stroke-width="1.3"/></svg>
        hello@tidewellpartners.uk
      </li>
      <li>
        <svg viewBox="0 0 16 16" aria-hidden="true"><circle cx="8" cy="8" r="6.5" fill="none" stroke="var(--accent-blue)" stroke-width="1.3"/><ellipse cx="8" cy="8" rx="3" ry="6.5" fill="none" stroke="var(--accent-blue)" stroke-width="1.1"/><path d="M1.5 8h13M2.5 4.8h11M2.5 11.2h11" stroke="var(--accent-blue)" stroke-width="1"/></svg>
        www.tidewellpartners.uk
      </li>
    </ul>
  </section>

  <section class="card card-back" aria-label="Business card back">
    <div class="brand">
      <span class="brand-dot"></span>
      <span class="brand-name">Tidewell Project Partners</span>
    </div>
  </section>
</main>
</body>
</html>
```